Website Redesign - home improvements/garage door supplier & installer in London

We are a garage door specialist providing installation, automation and repair services throughout the South East England with 5 branches/showrooms across London and over 65 employees. Garage doors are our main area of expertise but we have other home improvement products in our range - front/entrance doors, internal doors, sliding and bi-fold patio doors; awnings and shading systems.

Our current website is quite boring and uninviting so we are looking to redesign and modernise the whole site to improve the user experience and flow.
Responsive, desktop and mobile friendly.

www.brightwaygaragedoors.example

Main pages to be templated:

Homepage
Category pages/list e.g. https://www.brightwaygaragedoors.example/garage-doors/
Basic content/product pages e.g https://www.brightwaygaragedoors.example/veltrix-internal-doors/
Main services pages e.g. https://www.brightwaygaragedoors.example/garage-door-installation/
Branch pages e.g. https://www.brightwaygaragedoors.example/sidcup/
Contact page
-----------------------
Our logo must stay as is (the attached AI file has 3 elements - logo -BRIGHTWAY GARAGE DOORS with the 'B'mark, the SINCE 1976 mark and a tagline 'Far beyond your everyday garage doors' - these elements are to be used separately, not as a single block - although they can be combined)). Please use the text that’s already on the site in your design previews.
Our main colours are Blue RGB 35,57,119 and Red RGB 228,25,34

We would welcome a new smarter colour scheme but you will have to stick with the 2 primary colours we use on our logo - so any complimentary colours that might fit the new design would be great.

You can use all images that are on the website to support the new design - also attached is a zip with logo and images)

Target Market(s)

Most of our customers are in and around London - homeowners with garages that need servicing, replacing garage doors, upgrading or fitting new + other hiome improvements we can offer as listed above (fornt doors, bifold, sliding patio doors and awning) B2C

Industry/Entity Type

Home Improvement

Coding

Coded - Design and coding required

Font styles to use
Sans Serif

Requirements
Must have
• Custom and responsive design, user friendly, use our main 2 colours (red and blue described above) but add some complimentary colours to the mix
Nice to have
• Be creative, innovative
Should not have
• This should not be just some freely available wordpress template

```html
<!DOCTYPE html>
<html lang="en">
<head>
<meta charset="utf-8">
<title>Brightway Garage Doors – Garage Door Repairs in the South East</title>
<link href="https://fonts.googleapis.com/css2?family=Raleway:wght@600;700;800&family=Lato:wght@400;700;900&display=swap" rel="stylesheet">
<style>
:root{
  --blue:#233977;
  --navy:#223670;
  --red:#e41922;
  --ink:#333a45;
  --muted:#6b7280;
  --light:#efefef;
  --line:#d9dbe0;
  --white:#ffffff;
  --dark:#1f1f21;
}
*{box-sizing:border-box;margin:0;padding:0}
html,body{width:1200px;height:4569px;overflow:hidden}
body{position:relative;background:var(--white);font-family:"Lato",sans-serif;color:var(--ink)}
.abs{position:absolute}
h1,h2,h3{font-family:"Raleway",sans-serif}

/* header */
.site-header{left:0;top:0;width:1200px;height:124px;background:var(--white)}
.brand{left:80px;top:24px;display:flex;align-items:center;gap:10px}
.brand-dot{width:22px;height:22px;border-radius:50%;background:var(--blue)}
.brand-name{font-family:"Lato",sans-serif;font-weight:900;font-size:23px;color:var(--blue);line-height:1;white-space:nowrap}
.brand-tag{left:80px;top:58px;font-size:12px;font-weight:700;color:var(--blue);white-space:nowrap}
.callout{right:80px;top:24px;display:flex;align-items:center;gap:14px}
.callout-icon{width:44px;height:44px;border:2px solid var(--red);border-radius:50%;display:flex;align-items:center;justify-content:center}
.callout small{display:block;font-size:13px;font-weight:700;color:var(--ink);letter-spacing:.5px}
.callout strong{display:block;font-size:24px;font-weight:900;color:var(--red)}

/* hero */
.hero{left:0;top:122px;width:1200px;height:554px;background:linear-gradient(100deg,#3d3f43 0%,#6e7174 38%,#c9cacb 60%,#8d8f92 100%)}
.main-nav{left:128px;top:104px;width:912px;height:48px;background:var(--red);display:flex;justify-content:center;align-items:center;gap:26px;z-index:2}
.main-nav a{color:var(--white);font-size:14px;font-weight:700;text-decoration:none;letter-spacing:.3px}
.hero-title{left:80px;top:300px;font-size:46px;font-weight:800;color:var(--white);line-height:1.25;letter-spacing:.5px}
.hero-lead{left:80px;top:428px;width:460px;font-size:17px;font-weight:700;color:var(--white);line-height:1.6}

/* feature boxes */
.feature{width:305px;height:208px;background:#f4f4f5;padding:8px}
.feature-inner{width:100%;height:100%;background:var(--white);border:2px solid #c9ccd6;display:flex;flex-direction:column;align-items:center;justify-content:center;gap:28px}
.feature span{font-size:17px;font-weight:700;color:var(--ink);letter-spacing:.3px}

/* about */
.about{left:0;top:1050px;width:1200px;height:488px;background:var(--light)}
.about h2{left:80px;top:72px;font-size:40px;font-weight:700;color:var(--blue)}
.about p{left:80px;top:145px;width:520px;font-size:14px;line-height:1.75;color:#555}
.ticks{left:80px;top:302px;display:grid;grid-template-columns:300px 260px;row-gap:16px;font-size:15px;color:#444}
.ticks li{list-style:none;display:flex;align-items:center;gap:12px}
.about-art{left:700px;top:80px;width:445px;height:380px;background:linear-gradient(135deg,#f6fbfb,#cfe7e4 60%,#e9eeee)}

/* service band */
.service-band{left:0;top:1538px;width:1200px;height:183px;background:linear-gradient(90deg,#151515 0%,#2a2623 55%,#5a4536 100%)}
.service-band h2{left:80px;top:38px;font-size:28px;font-weight:800;color:var(--white);letter-spacing:.5px}
.service-band p{left:80px;top:86px;width:700px;font-size:15px;line-height:1.6;color:#e6e6e6}
.btn{background:var(--red);color:var(--white);font-family:"Lato",sans-serif;font-weight:900;font-size:17px;border-radius:30px;display:flex;align-items:center;justify-content:center;text-decoration:none;letter-spacing:.3px}

/* offers */
.offers-title{left:0;top:1766px;width:1200px;text-align:center;font-size:44px;font-weight:700;color:var(--blue)}
.offer{width:320px;height:353px;border:1px solid var(--line);background:var(--white)}
.offer-img{width:100%;height:276px}
.offer span{display:block;text-align:center;padding-top:28px;font-size:16px;font-weight:700;color:var(--ink);letter-spacing:.3px}

/* clients + testimonials */
.clients{left:0;top:2680px;width:1200px;height:420px;background:var(--light)}
.section-label{font-size:32px;font-weight:700;color:var(--blue)}
.arrows{display:flex;gap:10px}
.arrow{width:34px;height:34px;background:var(--navy);display:flex;align-items:center;justify-content:center}
.client-logo{width:238px;height:100px;background:var(--white);border:1px solid var(--line);display:flex;align-items:center;justify-content:center;font-size:26px;font-weight:900;color:var(--blue)}
.quote{left:624px;top:104px;width:497px;height:226px;background:var(--white);border:1px solid var(--line)}
.quote p{padding:26px 28px 0;font-size:15px;line-height:1.6;color:#555}
.quote-foot{left:0;bottom:0;width:100%;height:58px;background:var(--red)}
.quote-avatar{left:22px;bottom:22px;width:70px;height:70px;border-radius:50%;border:4px solid var(--white);background:linear-gradient(135deg,#a58064,#5d4433)}
.quote-foot span{left:110px;top:18px;color:var(--white);font-weight:900;font-size:17px}

/* cta band */
.cta-band{left:0;top:3100px;width:1200px;height:190px;background:linear-gradient(90deg,#2a1c16,#6a4a37 40%,#4b3628 70%,#2a1d17)}

/* callback form */
.callback h2{left:0;top:3330px;width:1200px;text-align:center;font-size:44px;font-weight:700;color:var(--blue)}
.field{width:356px;height:40px;border-bottom:1px solid #cfd2d8;font-size:15px;color:#8a8f98;padding-top:6px}

/* footer */
.site-footer{left:0;top:3762px;width:1200px;height:533px;background:var(--navy);color:var(--white)}
.foot-col h3{font-family:"Raleway",sans-serif;font-size:22px;font-weight:700;margin-bottom:18px}
.foot-col li{list-style:none;font-size:14px;line-height:2.15;color:#e3e7f2}
.foot-col h4{font-size:16px;font-weight:900;margin-top:14px}
.foot-col address{font-style:normal;font-size:14px;line-height:1.6;color:#e3e7f2}
.bottom-bar{left:0;top:4295px;width:1200px;height:274px;background:var(--dark)}
.socials{left:0;top:50px;width:1200px;display:flex;justify-content:center;gap:18px}
.social{width:50px;height:50px;border-radius:50%;background:var(--white)}
.copyright{left:0;top:188px;width:1200px;text-align:center;font-size:14px;color:#cfcfcf;letter-spacing:.3px}
</style>
</head>
<body>

<header class="abs site-header">
  <div class="abs brand"><div class="brand-dot"></div><div class="brand-name">BRIGHTWAY GARAGE DOORS</div></div>
  <div class="abs brand-tag">Far beyond your everyday garage doors</div>
  <div class="abs callout">
    <div class="callout-icon">
      <svg width="22" height="22" viewBox="0 0 24 24"><path d="M6.6 10.8a15.1 15.1 0 0 0 6.6 6.6l2.2-2.2a1 1 0 0 1 1-.25 11.4 11.4 0 0 0 3.6.57 1 1 0 0 1 1 1V20a1 1 0 0 1-1 1A17 17 0 0 1 3 4a1 1 0 0 1 1-1h3.5a1 1 0 0 1 1 1c0 1.25.2 2.45.57 3.57a1 1 0 0 1-.25 1z" fill="#e41922"/></svg>
    </div>
    <div><small>CALL US NOW</small><strong>0800 555 0142</strong></div>
  </div>
</header>

<section class="abs hero" role="img" aria-label="Modern white house with dark grey sectional garage doors and a silver car on the driveway"></section>
<nav class="abs main-nav">
  <a href="#">HOME</a><a href="#">OUR PRODUCTS</a><a href="#">INSTALLATION</a><a href="#">REPAIRS</a><a href="#">SPECIAL OFFER</a><a href="#">TESTIMONIALS</a><a href="#">CONTACT</a><a href="#">CAREER</a>
</nav>
<h1 class="abs hero-title">GARAGE DOOR REPAIRS<br>IN THE SOUTH EAST</h1>
<p class="abs hero-lead">We can repair virtually any manual manual or automatic garage door in the south east</p>

<div class="abs feature" style="left:85px;top:755px"><div class="feature-inner">
  <svg width="60" height="56" viewBox="0 0 60 56" fill="none" stroke="#233977" stroke-width="3"><path d="M4 22 30 4l26 18v30H4z"/><rect x="14" y="26" width="32" height="26"/><path d="M14 33h32M14 40h32M14 46h32"/></svg>
  <span>GARAGE DOOR TYPES</span></div></div>
<div class="abs feature" style="left:448px;top:755px"><div class="feature-inner">
  <svg width="54" height="58" viewBox="0 0 54 58" fill="none" stroke="#233977" stroke-width="3"><path d="M4 6l14 6v42L4 48zM18 12l18-8v42l-18 8zM36 4l14 6v42l-14-6z"/></svg>
  <span>BIFOLD DOORS</span></div></div>
<div class="abs feature" style="left:804px;top:755px"><div class="feature-inner">
  <svg width="58" height="58" viewBox="0 0 58 58" fill="none" stroke="#233977" stroke-width="4" stroke-linecap="round"><path d="M8 50 34 24M40 6a10 10 0 0 0-8 14l4 4a10 10 0 0 0 14-8l-6 2-4-6z"/><path d="M10 8l40 42M8 14l6-6"/></svg>
  <span>GARAGE DOOR REPAIRS</span></div></div>

<section class="abs about">
  <h2 class="abs">Brightway Garage Doors</h2>
  <p class="abs">Here at Brightway Garage Doors we've been putting our customers first for 40 years, providing thousands of garage doors throughout London and the South East. We work directly with leading manufacturers to bring you a premium garage door installation and repair facility. Our fully trained professional garage door installers and engineers provide friendly advice and a reliable service.</p>
  <ul class="abs ticks">
    <li><svg width="18" height="18" viewBox="0 0 18 18"><rect x="1" y="3" width="13" height="13" fill="none" stroke="#e41922" stroke-width="2"/><path d="M4 9l4 4 9-10" fill="none" stroke="#e41922" stroke-width="2.4"/></svg>Friendly helpful advice</li>
    <li><svg width="18" height="18" viewBox="0 0 18 18"><rect x="1" y="3" width="13" height="13" fill="none" stroke="#e41922" stroke-width="2"/><path d="M4 9l4 4 9-10" fill="none" stroke="#e41922" stroke-width="2.4"/></svg>Satisfaction guaranteed</li>
    <li><svg width="18" height="18" viewBox="0 0 18 18"><rect x="1" y="3" width="13" height="13" fill="none" stroke="#e41922" stroke-width="2"/><path d="M4 9l4 4 9-10" fill="none" stroke="#e41922" stroke-width="2.4"/></svg>FREE Estimates*</li>
    <li><svg width="18" height="18" viewBox="0 0 18 18"><rect x="1" y="3" width="13" height="13" fill="none" stroke="#e41922" stroke-width="2"/><path d="M4 9l4 4 9-10" fill="none" stroke="#e41922" stroke-width="2.4"/></svg>Affordable prices</li>
    <li><svg width="18" height="18" viewBox="0 0 18 18"><rect x="1" y="3" width="13" height="13" fill="none" stroke="#e41922" stroke-width="2"/><path d="M4 9l4 4 9-10" fill="none" stroke="#e41922" stroke-width="2.4"/></svg>Fully trained installers</li>
  </ul>
  <div class="abs about-art" role="img" aria-label="Up-and-over glass garage door shown half open on its frame"></div>
</section>

<section class="abs service-band" role="img" aria-label="Dark photo of a brick garage with timber doors">
  <h2 class="abs">UNRIVALLED SERVICE AT AFFORDABLE PRICES</h2>
  <p class="abs">At Brightway Garage Doors we pride ourselves on knowledgeable, friendly staff who will assist you in choosing the best automatic garage doors to suit your property and budget.</p>
  <a class="abs btn" href="#" style="left:852px;top:69px;width:270px;height:52px">FIND A SHOW ROOM</a>
</section>

<h2 class="abs offers-title">We also Offer</h2>
<div class="abs offer" style="left:79px;top:1834px"><div class="offer-img" role="img" aria-label="Wooden front entrance door with glazed side panels" style="background:linear-gradient(160deg,#8b8179,#4a2a1d 45%,#b7a894)"></div><span>FRONT DOOR</span></div>
<div class="abs offer" style="left:440px;top:1834px"><div class="offer-img" role="img" aria-label="Yellow retractable sun awning over a garden patio" style="background:linear-gradient(175deg,#b08a35,#d9c17a 30%,#6f8f4e 70%,#48663a)"></div><span>SUN AWNINGS</span></div>
<div class="abs offer" style="left:801px;top:1834px"><div class="offer-img" role="img" aria-label="Installer in a hi-vis vest fitting a garage door" style="background:linear-gradient(160deg,#dcdcd8,#b9b9b0 40%,#c9cc45 60%,#9a9a92)"></div><span>GARAGE DOOR INSTALLATION</span></div>
<div class="abs offer" style="left:79px;top:2233px"><div class="offer-img" role="img" aria-label="Weather seal strip being fitted across a garage floor" style="background:linear-gradient(160deg,#6a6a68,#a79c8f 50%,#5c544a)"></div><span>WEATHER DEFENDER</span></div>
<div class="abs offer" style="left:440px;top:2233px"><div class="offer-img" role="img" aria-label="Garage door spare parts: cables, springs and bars" style="background:linear-gradient(160deg,#f4f4f4,#e2e2e2 60%,#c94040 85%,#eeeeee)"></div><span>GARAGE DOOR SPARES</span></div>
<div class="abs offer" style="left:801px;top:2233px"><div class="offer-img" role="img" aria-label="Detached garage converted with double brown doors" style="background:linear-gradient(175deg,#9fb4c4,#cdd6d8 35%,#7a6a5c 60%,#4e5a3a)"></div><span>DOUBLE DOOR CONVERSION</span></div>

<section class="abs clients">
  <h2 class="abs section-label" style="left:79px;top:34px">Our Clients</h2>
  <div class="abs arrows" style="left:490px;top:40px">
    <div class="arrow"><svg width="14" height="14" viewBox="0 0 14 14"><path d="M9 2 4 7l5 5" stroke="#fff" stroke-width="2.4" fill="none"/></svg></div>
    <div class="arrow"><svg width="14" height="14" viewBox="0 0 14 14"><path d="M5 2l5 5-5 5" stroke="#fff" stroke-width="2.4" fill="none"/></svg></div>
  </div>
  <div class="abs client-logo" style="left:79px;top:104px">Harwell</div>
  <div class="abs client-logo" style="left:338px;top:104px">Oakridge</div>
  <div class="abs client-logo" style="left:79px;top:229px">Stanfield UK</div>
  <div class="abs client-logo" style="left:338px;top:229px">Solvane</div>

  <h2 class="abs section-label" style="left:624px;top:34px">Testimonials</h2>
  <div class="abs arrows" style="left:1043px;top:40px">
    <div class="arrow"><svg width="14" height="14" viewBox="0 0 14 14"><path d="M9 2 4 7l5 5" stroke="#fff" stroke-width="2.4" fill="none"/></svg></div>
    <div class="arrow"><svg width="14" height="14" viewBox="0 0 14 14"><path d="M5 2l5 5-5 5" stroke="#fff" stroke-width="2.4" fill="none"/></svg></div>
  </div>
  <div class="abs quote">
    <p>Lorem Ipsum is simply dummy text of the printing and typesetting industry. Lorem Ipsum has been the industry's standard dummy text ever since the 1500s, when an unknown printer took a galley of type and scrambled it to make.</p>
    <div class="abs quote-foot"><span class="abs">- CLIENT NAME</span></div>
    <div class="abs quote-avatar" role="img" aria-label="Client portrait"></div>
  </div>
</section>

<section class="abs cta-band" role="img" aria-label="Dark photo of timber garage doors">
  <a class="abs btn" href="#" style="left:277px;top:72px;width:318px;height:54px">DOWNLOAD BROCHURES</a>
  <a class="abs btn" href="#" style="left:612px;top:72px;width:312px;height:54px">REQUEST FREE SURVEY</a>
</section>

<section class="callback">
  <h2 class="abs">Requst a Call Back</h2>
  <div class="abs field" style="left:238px;top:3390px">Name</div>
  <div class="abs field" style="left:238px;top:3442px">Phone</div>
  <div class="abs field" style="left:238px;top:3496px">Email</div>
  <div class="abs field" style="left:238px;top:3548px">Postcode</div>
  <div class="abs field" style="left:630px;top:3390px;width:340px">Address</div>
  <div class="abs field" style="left:630px;top:3442px;width:340px;height:146px">Message</div>
  <a class="abs btn" href="#" style="left:490px;top:3626px;width:220px;height:50px">SUBMIT NOW</a>
</section>

<footer class="abs site-footer">
  <div class="abs foot-col" style="left:79px;top:46px">
    <h3>Garage Doors</h3>
    <ul><li>Garage Doors</li><li>Mechanism</li><li>Double Garage Door Conversion</li><li>Download a Brochure</li><li>Stock List</li><li>Garage Door Photo Gallery</li></ul>
    <h3 style="margin-top:22px">Showrooms</h3>
    <ul><li>Garage Door Showrooms</li><li>New Malden</li><li>Croydon</li><li>Sidcup</li><li>Watford</li><li>Upminster</li></ul>
  </div>
  <div class="abs foot-col" style="left:347px;top:46px">
    <h3>Guides</h3>
    <ul><li>How to Order</li><li>Choose The Door For You</li><li>Download a Brochure</li><li>Installation</li><li>Garage Door Repairs</li><li>Blog</li></ul>
  </div>
  <div class="abs foot-col" style="left:618px;top:46px">
    <h3>Helpful links</h3>
    <ul><li>About Us</li><li>Testimonials</li><li>FAQs</li><li>Request a Free Survey</li><li>Terms &amp; Conditions</li><li>Privacy Statement</li><li>Careers</li><li>Accreditations &amp; Certificates</li><li>Questionnaire</li><li>Trade Garage Doors</li><li>Garage Doors Spares</li><li>Garage Door Seal</li></ul>
  </div>
  <div class="abs foot-col" style="left:883px;top:46px;width:260px">
    <h3>Contact Us</h3>
    <h4 style="margin-top:0">Head Office Address:</h4>
    <address>Brightway Garage Doors Meridian House, Larkfield Way Crawley West Sussex RH10 4ZX</address>
    <h4>Phone:</h4><address>0800 555 0142</address>
    <h4>Email:</h4><address>crawley@brightwaygaragedoors.example</address>
    <h4>Showroom Opening Hours:</h4><address>Mon - Fri 7:30 AM - 5:00 PM<br>Sat 9:00 AM - 12:30 PM</address>
  </div>
</footer>

<div class="abs bottom-bar">
  <div class="abs socials">
    <span class="social" role="img" aria-label="Social profile link"></span>
    <span class="social" role="img" aria-label="Social profile link"></span>
    <span class="social" role="img" aria-label="Social profile link"></span>
    <span class="social" role="img" aria-label="Social profile link"></span>
    <span class="social" role="img" aria-label="Social profile link"></span>
    <span class="social" role="img" aria-label="Social profile link"></span>
    <span class="social" role="img" aria-label="Social profile link"></span>
  </div>
  <p class="abs copyright">©BRIGHTWAY GARAGE DOORS 2018 - All Rights Reserved.</p>
</div>

</body>
</html>
```